Zorvik Display Ads For Women (300x250 pixel)

We need ads for zorvik display. Please use the attached image to create GIF file ads. The ads needs to have the Quellmarket logo (attatched) and the slogan "Up To 80% Off Retail". The ads should have different background variation but the product or item should be center of attention.

Dimension: 300 by 250 pixel
File Type: GIF

Target Market(s)

Women

Industry/Entity Type

Zorvik

Font styles to use
Sans Serif

Requirements
Must have
• "View Now" button

```html
<!DOCTYPE html>
<html lang="en">
<head>
<meta charset="utf-8">
<title>Quellmarket Display Ads</title>
<link href="https://fonts.googleapis.com/css2?family=Roboto+Condensed:wght@300;700;800&display=swap" rel="stylesheet">
<style>
  :root {
    --page: #ffffff;
    --tab: #ffffff;
    --brand-ink: #2a2a2a;
    --plum-edge: #4f0f3b;
    --plum-mid: #7b2862;
    --plum-band: #5a1645;
    --plum-band-light: #8a3a72;
    --silver-edge: #9e9e9e;
    --silver-mid: #cfcfcf;
    --silver-band: #b8b8b8;
    --silver-band-light: #dcdcdc;
    --amber-edge: #e49f3b;
    --amber-mid: #f3c67e;
    --amber-band: #f0b865;
    --amber-band-light: #f8d9a6;
    --light-text: #ffffff;
    --dark-text: #3a3a3a;
    --amber-text: #b98236;
    --metal-silver: #c9ccd2;
    --metal-gold: #d9a54a;
    --metal-black: #2e2a2e;
    --stone-pink: #e56ab0;
    --stone-blue: #8ec9e6;
    --stone-clear: #f4f4f7;
  }
  * { margin: 0; padding: 0; box-sizing: border-box; }
  html, body {
    width: 1200px; height: 233px; overflow: hidden;
    background: var(--page);
    font-family: "Roboto Condensed", "Arial Narrow", sans-serif;
  }
  .ad-row { position: relative; width: 1200px; height: 233px; }
  .ad {
    position: absolute; top: 26px; width: 216px; height: 180px; overflow: hidden;
    background: radial-gradient(ellipse 60% 66% at 50% 44%, #ffffff 0%, #ffffff 24%, var(--mid) 64%, var(--edge) 100%);
  }
  .ad--plum   { --edge: var(--plum-edge);   --mid: var(--plum-mid);   --band: var(--plum-band);   --band-light: var(--plum-band-light);   --slogan: var(--light-text); }
  .ad--silver { --edge: var(--silver-edge); --mid: var(--silver-mid); --band: var(--silver-band); --band-light: var(--silver-band-light); --slogan: var(--dark-text); }
  .ad--amber  { --edge: var(--amber-edge);  --mid: var(--amber-mid);  --band: var(--amber-band);  --band-light: var(--amber-band-light);  --slogan: var(--amber-text); }

  .brand-tab {
    position: absolute; top: 0; left: 0; width: 132px; height: 32px;
    background: var(--tab);
    clip-path: polygon(0 0, 100% 0, 84% 100%, 0 100%);
    display: flex; align-items: center; gap: 5px; padding-left: 9px;
  }
  .brand-mark { width: 9px; height: 9px; background: var(--brand-ink); flex: none; }
  .brand-name {
    font-weight: 300; font-size: 16px; letter-spacing: -0.2px; color: var(--brand-ink); line-height: 1;
  }
  .product-photo {
    position: absolute; left: 74px; top: 42px; width: 68px; height: 100px;
    border-radius: 30px 30px 34px 34px;
    background: linear-gradient(180deg, var(--stone) 0%, var(--stone) 20%, var(--metal) 34%, var(--metal-2) 100%);
    box-shadow: 0 6px 10px rgba(0,0,0,0.12);
  }
  .product-photo--one   { --stone: var(--stone-pink);  --metal: var(--metal-silver); --metal-2: #a9adb6; }
  .product-photo--two   { --stone: var(--stone-clear); --metal: var(--metal-silver); --metal-2: var(--metal-gold); }
  .product-photo--three { --stone: var(--stone-pink);  --metal: #55505a; --metal-2: var(--metal-black); }
  .product-photo--four  { --stone: var(--stone-clear); --metal: #e9e6e0; --metal-2: var(--metal-gold); }
  .product-photo--five  { --stone: var(--stone-pink);  --metal: #4a4450; --metal-2: var(--metal-black); }

  .band { position: absolute; left: 0; bottom: 0; width: 216px; height: 62px; }
  .slogan {
    position: absolute; left: 0; right: 0; bottom: 10px; text-align: center;
    font-weight: 800; color: var(--slogan); white-space: nowrap; line-height: 1;
  }
  .slogan .small { font-size: 15px; font-weight: 700; }
  .slogan .big { font-size: 28px; letter-spacing: -0.6px; }
</style>
</head>
<body>
<main class="ad-row">

  <section class="ad ad--plum" style="left:23px">
    <div class="brand-tab"><span class="brand-mark"></span><span class="brand-name">QUELLMARKET</span></div>
    <div class="product-photo product-photo--one" role="img" aria-label="Silver ring with pink and blue stones"></div>
    <svg class="band" viewBox="0 0 216 62" aria-hidden="true">
      <path d="M0 16 C60 2 140 2 216 18 L216 62 L0 62 Z" fill="var(--band-light)" opacity="0.5"/>
      <path d="M0 24 C70 10 150 14 216 28 L216 62 L0 62 Z" fill="var(--band)"/>
    </svg>
    <p class="slogan"><span class="small">Up To </span><span class="big">80% Off</span><span class="small"> Retail</span></p>
  </section>

  <section class="ad ad--silver" style="left:258px">
    <div class="brand-tab"><span class="brand-mark"></span><span class="brand-name">QUELLMARKET</span></div>
    <div class="product-photo product-photo--two" role="img" aria-label="Twisted silver and gold ring with clear stone"></div>
    <svg class="band" viewBox="0 0 216 62" aria-hidden="true">
      <path d="M0 16 C60 2 140 2 216 18 L216 62 L0 62 Z" fill="var(--band-light)" opacity="0.6"/>
      <path d="M0 24 C70 10 150 14 216 28 L216 62 L0 62 Z" fill="var(--band)"/>
    </svg>
    <p class="slogan"><span class="small">Up To </span><span class="big">80% Off</span><span class="small"> Retail</span></p>
  </section>

  <section class="ad ad--plum" style="left:493px">
    <div class="brand-tab"><span class="brand-mark"></span><span class="brand-name">QUELLMARKET</span></div>
    <div class="product-photo product-photo--three" role="img" aria-label="Black ring set with pink flower stone"></div>
    <svg class="band" viewBox="0 0 216 62" aria-hidden="true">
      <path d="M0 16 C60 2 140 2 216 18 L216 62 L0 62 Z" fill="var(--band-light)" opacity="0.5"/>
      <path d="M0 24 C70 10 150 14 216 28 L216 62 L0 62 Z" fill="var(--band)"/>
    </svg>
    <p class="slogan"><span class="small">Up To </span><span class="big">80% Off</span><span class="small"> Retail</span></p>
  </section>

  <section class="ad ad--amber" style="left:728px">
    <div class="brand-tab"><span class="brand-mark"></span><span class="brand-name">QUELLMARKET</span></div>
    <div class="product-photo product-photo--four" role="img" aria-label="Gold ring with pave band and clear stone"></div>
    <svg class="band" viewBox="0 0 216 62" aria-hidden="true">
      <path d="M0 16 C60 2 140 2 216 18 L216 62 L0 62 Z" fill="var(--band-light)" opacity="0.6"/>
      <path d="M0 24 C70 10 150 14 216 28 L216 62 L0 62 Z" fill="var(--band)"/>
    </svg>
    <p class="slogan"><span class="small">Up To </span><span class="big">80% Off</span><span class="small"> Retail</span></p>
  </section>

  <section class="ad ad--plum" style="left:963px">
    <div class="brand-tab"><span class="brand-mark"></span><span class="brand-name">QUELLMARKET</span></div>
    <div class="product-photo product-photo--five" role="img" aria-label="Black ring set with pink stones"></div>
    <svg class="band" viewBox="0 0 216 62" aria-hidden="true">
      <path d="M0 16 C60 2 140 2 216 18 L216 62 L0 62 Z" fill="var(--band-light)" opacity="0.5"/>
      <path d="M0 24 C70 10 150 14 216 28 L216 62 L0 62 Z" fill="var(--band)"/>
    </svg>
    <p class="slogan"><span class="small">Up To </span><span class="big">80% Off</span><span class="small"> Retail</span></p>
  </section>

</main>
</body>
</html>
```